Verdant Turfworks by MO

Design a eye catching EDDM postcard for Lawn Care business... 6.5" x 8" EDDM Postcards with required bleed points

There are a few EDDM rules to follow which are.

1. Be sure to add your Postal Indicia it needs to read
“PRST STD ECRWSS U.S. POSTAGE PAID EDDM RETAIL”
in the top right area of your EDDM Flyer Postcard

2. The address area also needs to be filled in with
“****ECRWSS**** Local Postal Customer”

3. Both of these items need to be present on the same side for example both on the back of your EDDM mailer.
Please see the image on the side here for a visual description on how to set up your EDDM mailer correctly. (Attached Sample Template)

Target Market(s)

Home Owners that has a Lawn Care need

Industry/Entity Type

Lawn Care

Font styles to use
Serif

Colors

Designer to choose colors to be used in the design.

Requirements
Must have
• A beautiful background that capture the homeowner eyes when they open their mailbox and see this small card.
• My number: 713-554-0287
• My Name & Email: Malcolm Ostrander - maostgreens@quellmail.com

```html
<!DOCTYPE html>
<html lang="en">
<head>
<meta charset="utf-8">
<title>Verdant Turfworks by MO – EDDM Postcard</title>
<link rel="stylesheet" href="https://fonts.googleapis.com/css2?family=Oswald:wght@600;700&family=Arimo:wght@400;700&display=swap">
<style>
  :root {
    --board: #1c551c;
    --board-dark: #123d12;
    --board-label: #2a6a25;
    --band-dark: #2f6a14;
    --band-light: #5a9a22;
    --swoosh: #d6dc1c;
    --yellow: #ffd21a;
    --white: #ffffff;
    --ink: #1b1b1b;
    --leaf: #7cc225;
    --gold: #e0a416;
    --gold-dark: #a86d08;
    --pay-blue: #1d4f9a;
    --pay-note: #c22222;
  }
  * { box-sizing: border-box; margin: 0; padding: 0; }
  html, body { width: 1200px; height: 656px; overflow: hidden; }
  body {
    position: relative;
    background: radial-gradient(ellipse at 50% 40%, var(--board) 0%, var(--board-dark) 100%);
    font-family: "Arimo", Arial, sans-serif;
  }
  .board-label {
    position: absolute;
    color: var(--board-label);
    font-weight: 700;
    text-align: center;
  }
  .board-label--card { top: 70px; width: 512px; font-size: 14px; }
  .board-label--size { top: 550px; left: 0; width: 1200px; font-size: 29px; }

  .postcard {
    position: absolute;
    top: 100px;
    width: 512px;
    height: 416px;
    overflow: hidden;
    box-shadow: 0 2px 6px rgba(0,0,0,.45);
    border: 1px solid #5e9a33;
  }
  .postcard--plain { left: 70px; }
  .postcard--seal { left: 616px; }

  .hero-photo {
    position: absolute; inset: 0;
    background:
      linear-gradient(100deg, transparent 40%, rgba(150,205,70,.55) 75%, rgba(120,185,50,.8) 100%),
      linear-gradient(180deg, #d8d4c8 0%, #b8a48a 22%, #8f8a62 40%, #5b7a2e 58%, #6b3a22 70%, #72b23a 82%, #4e8a22 100%);
  }
  .band { position: absolute; inset: 0; width: 512px; height: 416px; }

  .brand {
    position: absolute; top: 0; left: 0;
    width: 212px; height: 80px;
    background: var(--white);
    border-bottom-right-radius: 90px 80px;
    display: flex; align-items: center; gap: 8px;
    padding-left: 18px;
  }
  .brand__name {
    font-weight: 700;
    font-size: 17px;
    line-height: 1.1;
    color: var(--ink);
  }
  .brand__dot { width: 12px; height: 12px; border-radius: 50%; background: var(--leaf); flex: none; }

  .indicia {
    position: absolute; top: 20px; left: 447px;
    width: 46px; height: 41px;
    background: var(--white);
    font-size: 5.6px; line-height: 1.15;
    text-align: center; color: var(--ink);
    padding-top: 4px;
  }
  .indicia b { font-weight: 700; }
  .mail-address {
    position: absolute; top: 69px; left: 369px;
    width: 124px; height: 35px;
    background: var(--white);
    font-size: 7px; line-height: 1.2; color: var(--ink);
    padding: 5px 6px;
  }
  .mail-address__route { font-size: 8px; }

  .inset-photo {
    position: absolute; left: 32px;
    width: 158px; height: 108px;
    border: 2px solid var(--white);
    border-radius: 6px 24px 24px 6px;
  }
  .inset-photo--front {
    top: 100px;
    background: linear-gradient(180deg, #a9c3d6 0%, #9aa0a6 30%, #8f4f2e 55%, #5fa532 72%, #3f8a22 100%);
  }
  .inset-photo--garden {
    top: 214px;
    background: linear-gradient(180deg, #dfe8ee 0%, #8a6a48 28%, #4f8f2e 55%, #d3c4a4 72%, #58a02c 100%);
  }

  .perks {
    position: absolute; left: 36px; top: 337px;
    list-style: none;
    color: var(--white);
    font-weight: 700; font-size: 14.5px; line-height: 16px;
  }
  .perks li { display: flex; align-items: center; gap: 6px; }
  .perks svg { flex: none; }

  .call {
    position: absolute; left: 205px; width: 310px; top: 305px;
    text-align: center;
    font-family: "Oswald", "Arial Narrow", sans-serif;
  }
  .call__prompt {
    color: var(--white); font-weight: 700; font-size: 32px; line-height: 36px;
    text-shadow: 0 2px 3px rgba(0,0,0,.45);
    transform: scaleX(.9);
  }
  .call__phone {
    color: var(--yellow); font-weight: 700; font-size: 47px; line-height: 50px;
    text-shadow: 0 2px 4px rgba(0,0,0,.5);
    transform: scaleX(1);
  }
  .call__email {
    font-family: "Arimo", Arial, sans-serif;
    color: var(--white); font-size: 14px; letter-spacing: .8px;
    margin-top: 2px;
  }

  .quality-seal { position: absolute; left: 174px; top: 234px; width: 100px; height: 100px; }

  .payment-box {
    position: absolute; left: 368px; top: 244px;
    width: 122px; height: 46px;
    background: var(--white);
    text-align: center; color: var(--ink);
    padding-top: 2px;
  }
  .payment-box__note { font-size: 4.6px; font-weight: 700; line-height: 1.15; }
  .payment-box__note em { font-style: normal; color: var(--pay-note); }
  .payment-box__name { font-size: 12px; font-weight: 700; color: var(--pay-blue); line-height: 16px; }
  .payment-box__cards { display: flex; justify-content: center; gap: 2px; }
  .payment-box__cards span { width: 14px; height: 9px; border-radius: 1px; }
</style>
</head>
<body>

<p class="board-label board-label--card" style="left:70px;">Design without Seal</p>
<p class="board-label board-label--card" style="left:616px;">Design with Seal and Tillspan Pay</p>

<section class="postcard postcard--plain">
  <div class="hero-photo" role="img" aria-label="Landscaped front yard with clipped hedges, mulch beds and green lawn before a house"></div>
  <svg class="band" viewBox="0 0 512 416" aria-hidden="true">
    <defs>
      <linearGradient id="bandA" x1="0" y1="0" x2="0" y2="1">
        <stop offset="0" stop-color="var(--band-light)"/>
        <stop offset="1" stop-color="var(--band-dark)"/>
      </linearGradient>
    </defs>
    <path d="M0,288 C160,300 360,268 512,222 L512,236 C360,282 160,312 0,302 Z" fill="var(--swoosh)"/>
    <path d="M0,300 C160,310 360,280 512,234 L512,416 L0,416 Z" fill="url(#bandA)"/>
  </svg>
  <div class="brand"><span class="brand__name">Verdant<br>Turfworks</span><span class="brand__dot"></span></div>
  <div class="indicia">PRST STD<br>ECRWSS<br>U.S. POSTAGE<br><b>PAID</b><br>EDDM RETAIL</div>
  <div class="mail-address"><div class="mail-address__route">******************ECRWSS****</div>Local<br>Postal Customer</div>
  <div class="inset-photo inset-photo--front" role="img" aria-label="Front yard with fresh mulch bed and young trees"></div>
  <div class="inset-photo inset-photo--garden" role="img" aria-label="Backyard garden with stepping-stone path and pergola"></div>
  <ul class="perks">
    <li><svg width="13" height="13" viewBox="0 0 13 13"><circle cx="6.5" cy="6.5" r="6.5" fill="var(--yellow)"/><path d="M3.5 6.8l2 2 4-4.4" stroke="var(--band-dark)" stroke-width="1.8" fill="none"/></svg>Free Estimates</li>
    <li><svg width="13" height="13" viewBox="0 0 13 13"><circle cx="6.5" cy="6.5" r="6.5" fill="var(--yellow)"/><path d="M3.5 6.8l2 2 4-4.4" stroke="var(--band-dark)" stroke-width="1.8" fill="none"/></svg>Owner Operated</li>
    <li><svg width="13" height="13" viewBox="0 0 13 13"><circle cx="6.5" cy="6.5" r="6.5" fill="var(--yellow)"/><path d="M3.5 6.8l2 2 4-4.4" stroke="var(--band-dark)" stroke-width="1.8" fill="none"/></svg>Reliable Services</li>
    <li><svg width="13" height="13" viewBox="0 0 13 13"><circle cx="6.5" cy="6.5" r="6.5" fill="var(--yellow)"/><path d="M3.5 6.8l2 2 4-4.4" stroke="var(--band-dark)" stroke-width="1.8" fill="none"/></svg>Licensed ans Insured</li>
  </ul>
  <div class="call">
    <div class="call__prompt">Call Us Now!</div>
    <div class="call__phone">713-554-0287</div>
    <div class="call__email">maostgreens@quellmail.com</div>
  </div>
</section>

<section class="postcard postcard--seal">
  <div class="hero-photo" role="img" aria-label="Landscaped front yard with clipped hedges, mulch beds and green lawn before a house"></div>
  <svg class="band" viewBox="0 0 512 416" aria-hidden="true">
    <defs>
      <linearGradient id="bandB" x1="0" y1="0" x2="0" y2="1">
        <stop offset="0" stop-color="var(--band-light)"/>
        <stop offset="1" stop-color="var(--band-dark)"/>
      </linearGradient>
    </defs>
    <path d="M0,288 C160,300 360,268 512,222 L512,236 C360,282 160,312 0,302 Z" fill="var(--swoosh)"/>
    <path d="M0,300 C160,310 360,280 512,234 L512,416 L0,416 Z" fill="url(#bandB)"/>
  </svg>
  <div class="brand"><span class="brand__name">Verdant<br>Turfworks</span><span class="brand__dot"></span></div>
  <div class="indicia">PRST STD<br>ECRWSS<br>U.S. POSTAGE<br><b>PAID</b><br>EDDM RETAIL</div>
  <div class="mail-address"><div class="mail-address__route">******************ECRWSS****</div>Local<br>Postal Customer</div>
  <div class="inset-photo inset-photo--front" role="img" aria-label="Front yard with fresh mulch bed and young trees"></div>
  <div class="inset-photo inset-photo--garden" role="img" aria-label="Backyard garden with stepping-stone path and pergola"></div>
  <svg class="quality-seal" viewBox="0 0 100 100" aria-hidden="true">
    <circle cx="50" cy="50" r="49" fill="var(--gold)"/>
    <circle cx="50" cy="50" r="40" fill="var(--gold-dark)"/>
    <circle cx="50" cy="50" r="30" fill="var(--gold)"/>
  </svg>
  <div class="payment-box">
    <div class="payment-box__note">Credit or debit card payment via Tillspan<br><em>(No Tillspan account needed!)</em></div>
    <div class="payment-box__name">Tillspan Pay</div>
    <div class="payment-box__cards">
      <span style="background:#1a3d8f"></span><span style="background:#2a5ca8"></span><span style="background:#e04a1c"></span><span style="background:#3b7fc4"></span><span style="background:#2b4fa0"></span><span style="background:#d7d7d7"></span>
    </div>
  </div>
  <ul class="perks">
    <li><svg width="13" height="13" viewBox="0 0 13 13"><circle cx="6.5" cy="6.5" r="6.5" fill="var(--yellow)"/><path d="M3.5 6.8l2 2 4-4.4" stroke="var(--band-dark)" stroke-width="1.8" fill="none"/></svg>Free Estimates</li>
    <li><svg width="13" height="13" viewBox="0 0 13 13"><circle cx="6.5" cy="6.5" r="6.5" fill="var(--yellow)"/><path d="M3.5 6.8l2 2 4-4.4" stroke="var(--band-dark)" stroke-width="1.8" fill="none"/></svg>Owner Operated</li>
    <li><svg width="13" height="13" viewBox="0 0 13 13"><circle cx="6.5" cy="6.5" r="6.5" fill="var(--yellow)"/><path d="M3.5 6.8l2 2 4-4.4" stroke="var(--band-dark)" stroke-width="1.8" fill="none"/></svg>Reliable Services</li>
    <li><svg width="13" height="13" viewBox="0 0 13 13"><circle cx="6.5" cy="6.5" r="6.5" fill="var(--yellow)"/><path d="M3.5 6.8l2 2 4-4.4" stroke="var(--band-dark)" stroke-width="1.8" fill="none"/></svg>Licensed ans Insured</li>
  </ul>
  <div class="call">
    <div class="call__prompt">Call Us Now!</div>
    <div class="call__phone">713-554-0287</div>
    <div class="call__email">maostgreens@quellmail.com</div>
  </div>
</section>

<p class="board-label board-label--size">8” x 6.5” EDDM PostCard Design</p>

</body>
</html>
```